Calder Pizza - Takeout Menu Design

We are looking for a takeout menu design.
We are looking for a( 5" x 8.5" DOUBLE SIDED) flyer with our available pizza flavors
Must be easy to ready and not "busy"

Must include our logo (attached)
website: www.calderpizza.ca
address:
Fenwick Ridge Plaza
417, 318 9 Avenue SW
and the following details:
Visit our website for our complete appetizer, pasta, salad and catering menu.

Winner of this contest will also be offered to create a few print designs via printhive.

Please do not hesitate to ask any questions.

Target Market(s)

Business / Office clientele

Industry/Entity Type

Pizza place / specializing in corporate orders

Requirements
Must have
• Easy to read
Should not have
• Can not be busy or cluttered

```html
<!DOCTYPE html>
<html lang="en">
<head>
<meta charset="utf-8">
<title>Calder Pizza – Takeout Menu</title>
<link href="https://fonts.googleapis.com/css2?family=Archivo+Black&family=Poppins:wght@300;400;600;700;800&display=swap" rel="stylesheet">
<style>
:root{
  --stage:#e9e9e9;
  --char:#1c1a1a;
  --char-deep:#111010;
  --red:#d9261a;
  --red-deep:#b3170f;
  --flame:#f2411a;
  --orange:#f5821f;
  --maroon:#2a0c06;
  --bar:#7a0d0d;
  --gold:#c9a21a;
  --hot:#e0161b;
  --yellow:#ffd21f;
  --white:#ffffff;
  --ink:#1a0d08;
}
*{margin:0;padding:0;box-sizing:border-box}
html,body{width:1200px;height:1020px;overflow:hidden}
body{background:var(--stage);font-family:"Poppins",sans-serif;position:relative}

.flyer{position:absolute;top:137px;width:451px;height:767px;overflow:hidden;
  background:linear-gradient(180deg,var(--char) 0%,var(--char-deep) 100%);color:var(--white)}
.flyer--front{left:133px}
.flyer--back{left:616px}
.red-field{position:absolute;inset:0;width:100%;height:100%}

/* front */
.brand{position:absolute;top:42px;left:0;width:100%;text-align:center;font-weight:300;font-size:29px;letter-spacing:1px;color:var(--white)}
.brand-dot{display:inline-block;width:12px;height:12px;border-radius:50%;background:var(--white);margin-left:8px;vertical-align:middle}
.headline{position:absolute;left:0;width:100%;text-align:center;font-family:"Archivo Black",sans-serif;line-height:1}
.headline--takeout{top:96px;font-size:60px;color:var(--red);letter-spacing:-1px}
.headline--menu{top:150px;font-size:88px;color:var(--white);letter-spacing:-2px}
.hero-photo{position:absolute;left:20px;top:225px;width:414px;height:205px;border-radius:50%;
  background:radial-gradient(ellipse at 60% 40%,#f0b45a 0%,#d9702c 45%,#8a3a18 80%,rgba(90,40,20,0) 100%)}
.classic-title{position:absolute;left:37px;top:461px;font-weight:800;font-size:21px;line-height:23px;text-transform:uppercase}
.classic-blurb{position:absolute;left:37px;top:565px;width:135px;font-size:14.5px;line-height:18px;font-weight:400}
.gst{font-size:9px;font-weight:400;color:var(--white)}
.classic-gst{position:absolute;left:37px;top:693px}

.size-tab{position:absolute;height:17px;background:var(--white);color:var(--ink);border-radius:6px 6px 0 0;
  font-weight:700;font-size:10px;text-align:center;line-height:18px}
.classic-row{position:absolute;left:180px;width:248px;height:24px;font-weight:700;font-size:11px}
.classic-row .name{position:absolute;left:0;top:0;width:131px;height:100%;background:var(--flame);border-radius:8px 0 0 8px;
  padding-left:12px;display:flex;align-items:center;line-height:13px}
.classic-row .p8{position:absolute;left:139px;top:0;width:51px;height:100%;background:var(--orange);color:var(--ink);
  display:flex;align-items:center;justify-content:center}
.classic-row .p13{position:absolute;left:195px;top:0;width:53px;height:100%;background:var(--maroon);border-radius:0 12px 12px 0;
  display:flex;align-items:center;justify-content:center}
.classic-row--tall{height:35px}

.order-bar{position:absolute;left:38px;top:718px;width:390px;height:24px;border:2px solid var(--yellow);border-radius:14px;
  display:flex;align-items:center;font-size:10px;letter-spacing:3px}
.order-bar .cta{width:178px;text-align:center;color:var(--yellow);font-weight:700}
.order-bar .divider{width:1px;height:14px;background:var(--yellow)}
.order-bar .site{flex:1;text-align:center;font-weight:400;font-size:12px;letter-spacing:2.5px}

/* back */
.spec-title{position:absolute;left:49px;top:28px;font-family:"Archivo Black",sans-serif;font-size:16px;letter-spacing:0;white-space:nowrap;line-height:1}
.spec-title span{color:var(--hot)}
.spec-tab{position:absolute;top:54px;width:40px;height:13px;background:var(--white);color:var(--ink);border-radius:5px 5px 0 0;
  font-size:8px;font-weight:700;text-align:center;line-height:14px}
.spec-row{position:absolute;height:14px;width:191px}
.spec-row .name{position:absolute;left:0;top:0;width:101px;height:14px;padding-left:7px;font-size:7.5px;font-weight:700;line-height:14px;
  background:linear-gradient(90deg,var(--bar) 0%,rgba(122,13,13,.55) 100%);border-radius:3px 0 0 3px;white-space:nowrap}
.spec-row .p8{position:absolute;left:106px;top:0;width:40px;height:14px;background:var(--gold);color:var(--ink);font-size:7.5px;font-weight:700;text-align:center;line-height:14px}
.spec-row .p13{position:absolute;left:151px;top:0;width:40px;height:14px;background:var(--hot);border-radius:0 7px 7px 0;font-size:7.5px;font-weight:700;text-align:center;line-height:14px}
.spec-row .desc{position:absolute;left:3px;top:16px;width:100px;font-size:6px;line-height:7px;font-weight:400}
.col-left .spec-row{left:26px}
.col-right .spec-row{left:233px}
.spec-photo{position:absolute;left:224px;top:556px;width:227px;height:141px;border-radius:30px 0 0 20px;
  background:radial-gradient(ellipse at 55% 45%,#f3c27a 0%,#d98a3c 50%,#8f4a1e 100%)}
.full-menu-note{position:absolute;left:29px;top:622px;width:185px;font-size:7.5px;line-height:9.5px;font-weight:600;color:var(--yellow)}
.address{position:absolute;left:38px;top:687px;display:flex;gap:6px;font-size:10px;line-height:12px}
.address svg{margin-top:1px}
.back-gst{position:absolute;left:338px;top:703px}
</style>
</head>
<body>

<section class="flyer flyer--front">
  <svg class="red-field" viewBox="0 0 451 767" preserveAspectRatio="none" aria-hidden="true">
    <defs>
      <linearGradient id="frontRed" x1="0" y1="0" x2="0" y2="1">
        <stop offset="0" stop-color="#c81d12"/><stop offset="1" stop-color="#e23a1c"/>
      </linearGradient>
    </defs>
    <path d="M0 356 L18 350 L30 362 L60 368 L120 378 L200 392 L260 398 L320 384 L360 372 L392 360 L420 352 L451 366 L451 767 L0 767 Z" fill="#ffffff"/>
    <path d="M0 364 L24 360 L40 372 L100 384 L180 398 L250 406 L320 394 L370 380 L410 368 L451 374 L451 767 L0 767 Z" fill="url(#frontRed)"/>
  </svg>

  <div class="brand">CALDER PIZZA<span class="brand-dot"></span></div>
  <div class="headline headline--takeout">TAKEOUT</div>
  <div class="headline headline--menu">MENU</div>
  <div class="hero-photo" role="img" aria-label="Photo of two pepperoni pizzas on a wooden board"></div>

  <h2 class="classic-title">Classic<br>Take-Out<br>Pizza<br>8" &amp; 13"</h2>
  <p class="classic-blurb">All of our pizzas are prepared fresh everyday using only the finest mozzarella blend and ingredients.</p>
  <p class="gst classic-gst">*GST Not Included</p>

  <div class="size-tab" style="left:319px;top:446px;width:51px">8″</div>
  <div class="size-tab" style="left:375px;top:446px;width:53px">13″</div>

  <div class="classic-row classic-row--tall" style="top:463px"><div class="name">Pepperoni &amp;<br>Mushroom</div><div class="p8">$12.99</div><div class="p13">$30.95</div></div>
  <div class="classic-row" style="top:504px"><div class="name">Pepperoni</div><div class="p8">$11.99</div><div class="p13">$29.95</div></div>
  <div class="classic-row" style="top:533px"><div class="name">Hawaiian</div><div class="p8">$12.99</div><div class="p13">$30.95</div></div>
  <div class="classic-row" style="top:562px"><div class="name">Beef &amp; Mushroom</div><div class="p8">$13.49</div><div class="p13">$32.95</div></div>
  <div class="classic-row" style="top:590px"><div class="name">Pepperoni &amp; Ham</div><div class="p8">$12.99</div><div class="p13">$30.95</div></div>
  <div class="classic-row" style="top:619px"><div class="name">Ham &amp; Mushroom</div><div class="p8">$12.99</div><div class="p13">$30.95</div></div>
  <div class="classic-row" style="top:648px"><div class="name">Beef &amp; Onion</div><div class="p8">$13.49</div><div class="p13">$32.95</div></div>
  <div class="classic-row" style="top:677px"><div class="name">Cheese</div><div class="p8">$11.99</div><div class="p13">$29.95</div></div>

  <div class="order-bar"><span class="cta">VISIT US TO ORDER</span><span class="divider"></span><span class="site">www.calderpizza.ca</span></div>
</section>

<section class="flyer flyer--back">
  <svg class="red-field" viewBox="0 0 451 767" preserveAspectRatio="none" aria-hidden="true">
    <path d="M0 644 L30 634 L60 640 L110 646 L150 656 L190 668 L230 676 L451 676 L451 767 L0 767 Z" fill="#ffffff"/>
    <path d="M0 652 L40 642 L100 652 L150 664 L200 678 L240 684 L451 684 L451 767 L0 767 Z" fill="#d42414"/>
  </svg>

  <h2 class="spec-title">SPECIALITY TAKE-OUT PIZZA <span>8" &amp; 13"</span></h2>

  <div class="spec-tab" style="left:132px">8″</div>
  <div class="spec-tab" style="left:177px">13″</div>
  <div class="spec-tab" style="left:340px">8″</div>
  <div class="spec-tab" style="left:385px">13″</div>

  <div class="col-left">
    <div class="spec-row" style="top:70px"><div class="name">All Meat</div><div class="p8">$14.99</div><div class="p13">$35.95</div><p class="desc">Pepperoni, Beef &amp; Smoked Ham &amp; Bacon</p></div>
    <div class="spec-row" style="top:108px"><div class="name">Double Pepperoni</div><div class="p8">$13.49</div><div class="p13">$32.95</div><p class="desc">Loads of Pepperoni</p></div>
    <div class="spec-row" style="top:138px"><div class="name">Hot Honey Pepperoni</div><div class="p8">$14.49</div><div class="p13">$34.95</div><p class="desc">Double Pepperoni and drizzled with Hot Honey</p></div>
    <div class="spec-row" style="top:175px"><div class="name">Hawaiian Heat</div><div class="p8">$13.49</div><div class="p13">$32.95</div><p class="desc">Smoked Ham, Pineapple and Banana Peppers</p></div>
    <div class="spec-row" style="top:214px"><div class="name">Four Cheese</div><div class="p8">$13.49</div><div class="p13">$32.95</div><p class="desc">Mozzarella, Feta, Romano and Cheddar Cheese</p></div>
    <div class="spec-row" style="top:253px"><div class="name">Montreal</div><div class="p8">$13.49</div><div class="p13">$32.95</div><p class="desc">Pepperoni &amp; Double Smoked Bacon</p></div>
    <div class="spec-row" style="top:290px"><div class="name">Montreal Heat</div><div class="p8">$13.49</div><div class="p13">$33.95</div><p class="desc">Pepperoni, Double Smoked Bacon &amp; Banana Peppers</p></div>
    <div class="spec-row" style="top:333px"><div class="name">Supreme</div><div class="p8">$13.49</div><div class="p13">$33.95</div><p class="desc">Pepperoni, Mushrooms &amp; Green Peppers</p></div>
    <div class="spec-row" style="top:374px"><div class="name">Canadian</div><div class="p8">$13.49</div><div class="p13">$33.95</div><p class="desc">Pepperoni, Mushrooms &amp; Ham</p></div>
    <div class="spec-row" style="top:409px"><div class="name">BBQ Chicken</div><div class="p8">$13.49</div><div class="p13">$33.95</div><p class="desc">Chicken Breast, Hickory BBQ Sauce &amp; Red Onions</p></div>
    <div class="spec-row" style="top:450px"><div class="name">BBQ Chicken Plus</div><div class="p8">$13.49</div><div class="p13">$33.95</div><p class="desc">Chicken Breast, Hickory BBQ Sauce, Red Onions &amp; Cilantro</p></div>
    <div class="spec-row" style="top:495px"><div class="name">Spicy BBQ Chicken</div><div class="p8">$13.49</div><div class="p13">$33.95</div><p class="desc" style="width:120px">Chicken Breast, Hickory BBQ Sauce, Red Onions &amp; Banana Peppers</p></div>
    <div class="spec-row" style="top:538px"><div class="name">Chicken Club</div><div class="p8">$13.49</div><div class="p13">$33.95</div><p class="desc" style="width:120px">Chicken Breast, Double Smoked Bacon, Red Onions and Tomatoes</p></div>
    <div class="spec-row" style="top:585px"><div class="name">Athenean</div><div class="p8">$13.49</div><div class="p13">$33.95</div><p class="desc">Chicken Breast, Spinach, Feta Cheese and Tomato</p></div>
  </div>

  <div class="col-right">
    <div class="spec-row" style="top:70px"><div class="name">Sweet Chili Chicken</div><div class="p8">$14.99</div><div class="p13">$35.95</div><p class="desc">Chicken Breast, Pineapple, Red Onions &amp; Sweet Chili Sauce</p></div>
    <div class="spec-row" style="top:112px"><div class="name">Greek Supreme</div><div class="p8">$14.99</div><div class="p13">$35.95</div><p class="desc" style="width:120px">Chicken Breast, Feta Cheese, Tomato, Green Pepper, Red Onions &amp; Black Olives</p></div>
    <div class="spec-row" style="top:153px"><div class="name">Original Spinach</div><div class="p8">$14.99</div><div class="p13">$35.95</div><p class="desc">Spinach &amp; Feta Cheese</p></div>
    <div class="spec-row" style="top:187px"><div class="name">Mediterranean Chicken</div><div class="p8">$14.99</div><div class="p13">$35.95</div><p class="desc" style="width:115px">Seasoned Chicken Breast, Tomatoes, Red Onions and Feta Cheese</p></div>
    <div class="spec-row" style="top:229px"><div class="name">Zeus</div><div class="p8">$14.99</div><div class="p13">$35.95</div><p class="desc" style="width:120px">Spinach, Feta Cheese and Tomatoes</p></div>
    <div class="spec-row" style="top:264px"><div class="name">Greek</div><div class="p8">$14.99</div><div class="p13">$35.95</div><p class="desc" style="width:120px">Feta Cheese, Tomato, Green Peppers, Red Onions and Black Olives</p></div>
    <div class="spec-row" style="top:306px"><div class="name">Vegetarian</div><div class="p8">$14.99</div><div class="p13">$35.95</div><p class="desc">Mushrooms, Tomatoes, Green Peppers and Black Olives</p></div>
    <div class="spec-row" style="top:348px"><div class="name">Veggie Delight</div><div class="p8">$14.99</div><div class="p13">$35.95</div><p class="desc">Mushrooms, Tomatoes, Green Peppers, Black Olives &amp; Onions</p></div>
    <div class="spec-row" style="top:391px"><div class="name">Deluxe</div><div class="p8">$14.99</div><div class="p13">$35.95</div><p class="desc" style="width:120px">Pepperoni, Mushrooms, Ham, Tomatoes, Green Peppers and Red Onions</p></div>
    <div class="spec-row" style="top:431px"><div class="name">Calder Special</div><div class="p8">$14.99</div><div class="p13">$35.95</div><p class="desc" style="width:130px">Pepperoni, Mushrooms, Ham, Green Peppers and Black Olives</p></div>
    <div class="spec-row" style="top:471px"><div class="name">Dill Pickle</div><div class="p8">$14.99</div><div class="p13">$35.95</div><p class="desc" style="width:115px">Crispy Dill Pickles, Fresh Dill with our cream based garlic sauce. Served with our without bacon</p></div>
    <div class="spec-row" style="top:519px"><div class="name">BBQ Pulled Pork</div><div class="p8">$14.99</div><div class="p13">$35.95</div><p class="desc">Pulled Pork, Red Onions, Red Peppers and Cilantro</p></div>
  </div>

  <div class="spec-photo" role="img" aria-label="Photo of a supreme pizza with a slice pulled out"></div>

  <p class="full-menu-note">Visit our website for our complete appetizer, pasta, salad and catering menu.</p>

  <div class="address">
    <svg width="9" height="12" viewBox="0 0 9 12" aria-hidden="true"><path d="M4.5 0A4.5 4.5 0 0 0 0 4.5C0 8 4.5 12 4.5 12S9 8 9 4.5A4.5 4.5 0 0 0 4.5 0Zm0 6.3a1.8 1.8 0 1 1 0-3.6 1.8 1.8 0 0 1 0 3.6Z" fill="#ffd21f"/></svg>
    <p>Fenwick Ridge Plaza<br>417, 318 9 Avenue SW</p>
  </div>
  <p class="gst back-gst">*GST Not Included</p>

  <div class="order-bar"><span class="cta">VISIT US TO ORDER</span><span class="divider"></span><span class="site">www.calderpizza.ca</span></div>
</section>

</body>
</html>
```